Stretch Depot Community Wordpress Site

Branding package: http://www.stretchdepot.example/drop/Stretch_Depot_Branding_v02.pdf
**please reference above branding package when creating theme.
The goal is to have the site come off industrious and functional. A warehouse feel without being too cold.
We are looking for a theme/skin for our wordpress site. The blog has already been setup and all necessary plugins have been installed.
Stretch Depot is the local yoga enthusiasts online portal for information regarding yoga in the community. It is a place to share experiences, events, knowledge, and encouragement, ultimately serving to build community and connect people in their love for the practice of yoga.
Work with the concept of a warehouse, it is a warehouse of ideas.
Some keywords that describe the site:
Energetic, friendly, welcoming, industrious, fun, confident, charming, grounded, functional.
Color Palette: http://www.stretchdepot.example/drop/color-palette.png
Logo: http://www.stretchdepot.example/drop/logo.png
Reason: Have not found something that is a good fit.
Target Market(s)
Predominantly women, mid 20s to mid 40s however appeals to anyone one looking for yoga in the area and while its predominantly females the site should have a masculine look.
Industry/Entity Type
Events
Requirements
Must have
- Must use the color palette
Must use provided logo
Should not have
- plain white background.

```html
<!DOCTYPE html>
<html lang="en">
<head>
<meta charset="utf-8">
<title>Stretch Depot</title>
<link href="https://fonts.googleapis.com/css2?family=Arimo:wght@400;700&family=Roboto+Condensed:wght@400&display=swap" rel="stylesheet">
<style>
:root{
  --brick:#7a4a3c;
  --brick-dark:#5a3329;
  --plum:#6e2a6c;
  --plum-light:#8a3f88;
  --page:#2b2727;
  --footer:#1b1919;
  --text:#b9b3b3;
  --text-dim:#8f8a8a;
  --white:#ffffff;
  --nav-active:#1d4a6a;
  --nav-text:#6fa8d6;
  --thumb:#121111;
}
*{box-sizing:border-box;margin:0;padding:0}
html,body{width:1174px;height:1200px;overflow:hidden;background:var(--page);font-family:"Arimo",Arial,sans-serif;color:var(--text)}
.canvas{position:relative;width:1174px;height:1200px;overflow:hidden;background:var(--page)}
.brick{position:absolute;left:0;width:1174px;background:linear-gradient(180deg,#8b5646 0%,var(--brick) 45%,var(--brick-dark) 100%)}
.brick--top{top:0;height:170px}
.brick--bottom{top:1116px;height:84px;background:linear-gradient(180deg,var(--brick-dark),var(--brick) 60%,#6a3e32)}
.brand{position:absolute;left:100px;top:58px;font-size:48px;font-weight:700;color:var(--plum);letter-spacing:-1px;line-height:1}
.brand-mark{display:inline-block;width:20px;height:20px;background:var(--plum);margin-right:12px;vertical-align:middle}
.tagline{position:absolute;right:46px;top:64px;font-size:42px;color:var(--plum-light);letter-spacing:-2px;text-shadow:0 1px 0 #d7b6d4}
.social{position:absolute;right:55px;top:8px;display:flex;gap:14px}
.social span{width:34px;height:34px;border-radius:4px;background:linear-gradient(#e8e8e8,#b9b9b9);box-shadow:0 1px 2px rgba(0,0,0,.5)}
.nav-band{position:absolute;top:170px;left:0;width:1174px;height:76px;background:linear-gradient(180deg,#1f1d1d,#2e2a2a 60%,#3a3535)}
.nav{position:absolute;left:143px;top:189px;width:902px;height:37px;border-radius:4px;background:linear-gradient(#2a2727,#141313);box-shadow:0 0 0 1px #4a4545,0 2px 4px rgba(0,0,0,.6);display:flex;align-items:center;padding-left:20px;font-family:"Roboto Condensed","Arial Narrow",sans-serif;font-size:21px}
.nav a{color:var(--nav-text);text-decoration:none;padding:0 21px;line-height:35px}
.nav a.is-active{background:var(--nav-active);color:var(--white);padding:0 12px;margin-right:20px}
.slider{position:absolute;left:74px;top:277px;width:1026px;height:356px;background:#0c0b0b;border-radius:8px;padding:7px}
.slide{width:100%;height:100%;border-radius:4px;background:radial-gradient(ellipse at 50% 55%,#f3efe9 0%,#ffffff 55%),#fff}
.arrow{position:absolute;top:430px;width:30px;height:50px;background:#0e0d0d}
.arrow--prev{left:46px;border-radius:25px 0 0 25px}
.arrow--next{left:1098px;border-radius:0 25px 25px 0}
.arrow svg{position:absolute;top:15px;left:8px}
.col{position:absolute;top:660px;font-size:13px;line-height:19px}
.col h2{font-size:15px;font-weight:400;color:var(--white);margin-bottom:26px}
.col--about{left:53px;width:330px;text-align:justify;letter-spacing:-0.1px}
.col--events{left:422px;width:333px}
.col--gallery{left:802px;width:326px}
.divider{position:absolute;top:645px;width:1px;height:260px;background:#3a3535}
.event{position:relative;text-align:justify;padding-bottom:7px;margin-bottom:9px;border-bottom:1px dotted #5a5555}
.event:last-child{border:none}
.more{position:absolute;right:0;font-size:11px;color:var(--text-dim);line-height:13px}
.event .more{bottom:9px}
.gal-item{display:flex;gap:12px;margin-bottom:11px;height:50px}
.thumb{width:82px;height:50px;background:var(--thumb);flex:none}
.gal-item p{position:relative;font-size:13px;line-height:19px;margin-top:-5px;width:232px;height:38px}
.gal-item .more{bottom:2px}
.btn{position:absolute;top:929px;width:115px;height:33px;border-radius:3px;background:linear-gradient(#5a5555,#3a3636);box-shadow:0 0 0 1px #777,0 2px 3px rgba(0,0,0,.6);color:#e6e2e2;font-size:13px;font-weight:700;text-align:center;line-height:33px}
.footer{position:absolute;top:980px;left:0;width:1174px;height:136px;background:var(--footer);font-size:11.5px}
.fcol{position:absolute;top:22px}
.fcol h3{font-size:12px;font-weight:400;color:var(--text);margin-bottom:9px;display:flex;align-items:center;gap:10px}
.fcol h3 i{display:block;height:1px;background:#555}
.fcol li{list-style:none;line-height:19px;color:var(--text)}
.fcol li b{font-weight:400;display:inline-block;width:38px;color:var(--text-dim)}
.contact li{display:flex;align-items:center;gap:12px;line-height:32px;color:var(--text-dim)}
.bottom-nav{position:absolute;top:1146px;left:323px;display:flex;gap:24px;font-size:11px;color:#fff;text-shadow:0 1px 1px #000}
.copy{position:absolute;top:1176px;left:536px;font-size:11px;color:#fff;text-shadow:0 1px 1px #000}
</style>
</head>
<body>
<div class="canvas">
  <div class="brick brick--top" role="img" aria-label="Red brick wall texture"></div>
  <div class="brand"><span class="brand-mark"></span>Stretch Depot</div>
  <div class="social"><span></span><span></span><span></span><span></span></div>
  <div class="tagline">Lorem ipsum dolor sit amet</div>

  <div class="nav-band"></div>
  <nav class="nav">
    <a class="is-active">Home</a><a>Calendar</a><a>About Us</a><a>Yogi of the month</a><a>Ask a Guru</a><a>Gallery</a><a>Contact Us</a>
  </nav>

  <div class="arrow arrow--prev"><svg width="14" height="20"><path d="M12 2 L3 10 L12 18" stroke="#ddd" stroke-width="3" fill="none"/></svg></div>
  <div class="slider"><div class="slide" role="img" aria-label="Woman in white sitting cross-legged in meditation on a bamboo mat with candles and a red vase"></div></div>
  <div class="arrow arrow--next"><svg width="14" height="20"><path d="M2 2 L11 10 L2 18" stroke="#ddd" stroke-width="3" fill="none"/></svg></div>

  <section class="col col--about">
    <h2>ABOUT THE COMPANY</h2>
    <p>Lorem ipsum dolor sit amet, consectetur adipisicing elit, sed do eiusmod tempor incididunt ut labore et dolore magna aliqua. Ut enim ad minim veniam, quis nostrud exercitation ullamco laboris nisi ut aliquip ex ea commodo consequat. Duis aute irure dolor in reprehenderit in voluptate velit esse cillum dolore eu fugiat nulla pariatur. Excepteur sint occaecat cupidatat non proident, sunt in culpa qui officia deserunt mollit anim id est laborum.</p>
  </section>
  <div class="divider" style="left:400px"></div>
  <section class="col col--events">
    <h2>UPCOMING EVENTS</h2>
    <div class="event">Lorem ipsum dolor sit amet, consectetur adipisicing elit, sed do eiusmod tempor incididunt ut labore et dolore magna aliqua.<span class="more">more</span></div>
    <div class="event">Lorem ipsum dolor sit amet, consectetur adipisicing elit, sed do eiusmod tempor incididunt ut labore et dolore magna aliqua.<span class="more">more</span></div>
    <div class="event">Lorem ipsum dolor sit amet, consectetur adipisicing elit, sed do eiusmod tempor incididunt ut labore et dolore magna aliqua.<span class="more">more</span></div>
  </section>
  <div class="divider" style="left:778px"></div>
  <section class="col col--gallery">
    <h2>GALLERY....</h2>
    <div class="gal-item"><div class="thumb"></div><p>Lorem ipsum dolor sit amet, consectetur adipisicing elit,<span class="more">more</span></p></div>
    <div class="gal-item"><div class="thumb"></div><p>Lorem ipsum dolor sit amet, consectetur adipisicing elit,<span class="more">more</span></p></div>
    <div class="gal-item"><div class="thumb"></div><p>Lorem ipsum dolor sit amet, consectetur adipisicing elit,<span class="more">more</span></p></div>
    <div class="gal-item"><div class="thumb"></div><p>Lorem ipsum dolor sit amet, consectetur adipisicing elit,<span class="more">more</span></p></div>
  </section>

  <div class="btn" style="left:263px">Read More</div>
  <div class="btn" style="left:637px">Read More</div>
  <div class="btn" style="left:1007px">Read More</div>

  <footer class="footer">
    <div class="fcol" style="left:45px">
      <h3>RECENT POST <i style="width:216px"></i></h3>
      <ul>
        <li><b>----</b>Lorem ipsum dolor sit amet, consectetur adipisicing</li>
        <li><b>----</b>Lorem ipsum dolor sit amet, consectetur adipisicing</li>
        <li><b>----</b>Lorem ipsum dolor sit amet, consectetur adipisicing</li>
        <li><b>----</b>Lorem ipsum dolor sit amet, consectetur adipisicing</li>
      </ul>
    </div>
    <div class="fcol" style="left:454px">
      <h3>CATEGORIES <i style="width:100px"></i></h3>
      <ul>
        <li><b>----</b>Lorem ipsum dolor sit amet.</li>
        <li><b>----</b>Lorem ipsum dolor sit amet.</li>
        <li><b>----</b>Lorem ipsum dolor sit amet.</li>
        <li><b>----</b>Lorem ipsum dolor sit amet.</li>
      </ul>
    </div>
    <div class="fcol" style="left:763px">
      <h3>META</h3>
      <ul><li>Log in</li><li>Entries RSS</li><li>Comments RSS</li><li>Blogpress.example</li></ul>
    </div>
    <div class="fcol contact" style="left:952px;top:14px">
      <h3>CONTACT US</h3>
      <ul>
        <li><svg width="22" height="16"><rect x="1" y="3" width="20" height="12" fill="#ccc"/><path d="M1 3 L11 10 L21 3" stroke="#555" fill="none"/></svg>abc@stretchdepot.example</li>
        <li><svg width="22" height="16"><path d="M6 1 C2 4 4 12 12 15 L14 12 L11 10 L9 11 C7 9 6 7 7 5 L8 3 Z" fill="#ccc"/></svg>0000000000</li>
        <li><svg width="22" height="16"><rect x="4" y="0" width="14" height="16" fill="#ccc"/><path d="M11 3 V11 M7 8 L11 12 L15 8" stroke="#333" stroke-width="2" fill="none"/></svg>Download</li>
      </ul>
    </div>
  </footer>

  <div class="brick brick--bottom" role="img" aria-label="Red brick wall texture"></div>
  <nav class="bottom-nav"><span>Home</span><span>Calendar</span><span>About Us</span><span>Yogi of the month</span><span>Ask a Guru</span><span>Gallery</span><span>Contact Us</span></nav>
  <div class="copy">© Stretch Depot</div>
</div>
</body>
</html>
```